Sydney law firm, Pelbury Solicitors, needs a flyer design!

We need a flyer design for our law firm which has been operating in Sydney for over 35 years. We want to send the flyer out to potential clients and also to existing clients to let them know the range of services that we provide. Our corporate colours are white, red and black and we would like these incorporated somewhat. The final design should be clean, modern and professional.

We would like the design to fit a double sided flyer approx. 210mm high x 100mm wide.

Law Firm

Serif
Sans Serif

eb2026
ffffff

• Details needed on the flyer are:
• Pelbury Solicitors
• 3/82 Tarrow Street, Liverpool, NSW 2170
• (02) 9413 5862
• www.pelburysolicitors-example.com.au
• info@pelburysolicitors-example.com.au
• Our areas of practice include:
• Property Law
• Conveyancing
• Leases
• Criminal Law
• Family Law
• Litigation and Dispute Resolution
• Company Law
• Wills and Estates
• Powers of Attorney and Guardianship
• a picture of scales or a picture of a gavel

```html
<!DOCTYPE html>
<html lang="en">
<head>
<meta charset="utf-8">
<title>Pelbury Solicitors – Flyer</title>
<link href="https://fonts.googleapis.com/css2?family=Cinzel:wght@400;500&family=Montserrat:wght@400;500;700;800&display=swap" rel="stylesheet">
<style>
:root{
  --red:#eb2026;
  --white:#ffffff;
  --black:#0b0b0b;
  --ink:#1c1c1c;
  --stage-top:#4a4a4a;
  --stage-bottom:#161616;
}
*{box-sizing:border-box;margin:0;padding:0}
html,body{width:1167px;height:1200px;overflow:hidden}
body{
  position:relative;
  background:radial-gradient(ellipse at 50% 30%,var(--stage-top) 0%,#2a2a2a 55%,var(--stage-bottom) 100%);
  font-family:"Montserrat",Arial,sans-serif;
}
.flyer{
  position:absolute;top:68px;width:507px;height:1064px;
  background:var(--white);
  box-shadow:0 8px 26px rgba(0,0,0,.55);
  display:flex;flex-direction:column;
}
.flyer--services{left:60px}
.flyer--about{left:598px}

.brand{
  height:175px;display:flex;flex-direction:column;align-items:center;justify-content:center;
  font-family:"Cinzel",Georgia,serif;font-weight:400;color:var(--ink);
}
.brand__name{font-size:58px;letter-spacing:1px;line-height:1}
.brand__sub{font-size:19px;letter-spacing:15px;margin-top:14px;padding-left:15px}

.banner{
  height:177px;background:var(--red);color:var(--white);
  display:flex;align-items:center;justify-content:center;text-align:center;
}
.banner__title{font-family:"Cinzel",Georgia,serif;font-weight:400;font-size:60px;line-height:1.02}
.banner__lead{font-weight:800;font-size:27px;line-height:1.35}

.columns-photo{
  position:relative;height:549px;
  background:linear-gradient(90deg,#8d8d8d 0%,#e2e2e2 18%,#bdbdbd 30%,#d9d9d9 55%,#a9a9a9 75%,#cfcfcf 100%);
}
.services{
  position:absolute;left:103px;top:34px;width:300px;list-style:none;
  display:flex;flex-direction:column;gap:10px;
}
.services li{
  background:rgba(255,255,255,.82);
  text-align:center;font-weight:700;font-size:21px;line-height:28px;color:var(--ink);
  padding:4px 6px;
}

.handshake-photo{
  height:330px;
  background:linear-gradient(120deg,#2a2a2a 0%,#6f6f6f 35%,#bdbdbd 55%,#5a5a5a 75%,#1d1d1d 100%);
}
.about{
  height:219px;background:var(--black);color:var(--white);
  padding:28px 55px 0 55px;font-size:16.5px;line-height:1.38;text-align:justify;
}
.about p+p{margin-top:9px}

.contact{
  flex:1;display:flex;flex-direction:column;align-items:center;justify-content:flex-start;
  padding-top:14px;text-align:center;color:var(--ink);
}
.contact__address{font-weight:700;font-size:19.5px}
.contact__phone{font-weight:800;font-size:33px;color:var(--red);margin-top:6px;line-height:1.1}
.contact__line{font-size:16px;line-height:1.3}
.flyer__base{height:26px;background:var(--black)}
</style>
</head>
<body>

<section class="flyer flyer--services">
  <header class="brand">
    <span class="brand__name">PELBURY</span>
    <span class="brand__sub">SOLICITORS</span>
  </header>
  <div class="banner"><h1 class="banner__title">WE CAN HELP<br>YOU WITH...</h1></div>
  <div class="columns-photo" role="img" aria-label="Black and white photograph of classical stone columns">
    <ul class="services">
      <li>Property Law</li>
      <li>Conveyancing</li>
      <li>Leases</li>
      <li>Criminal Law</li>
      <li>Family Law</li>
      <li>Litigation and<br>Dispute Resolution</li>
      <li>Company Law</li>
      <li>Wills and Estates</li>
      <li>Powers of Attorney<br>and Guardianship</li>
    </ul>
  </div>
  <footer class="contact">
    <p class="contact__address">3/82 Tarrow Street, Liverpool, NSW 2170</p>
    <p class="contact__phone">(02) 9413 5862</p>
    <p class="contact__line">www.pelburysolicitors-example.com.au</p>
    <p class="contact__line">info@pelburysolicitors-example.com.au</p>
  </footer>
  <div class="flyer__base"></div>
</section>

<section class="flyer flyer--about">
  <header class="brand">
    <span class="brand__name">PELBURY</span>
    <span class="brand__sub">SOLICITORS</span>
  </header>
  <div class="banner"><h2 class="banner__lead">Established For Over 30 Years,<br>You Can Feel Confident<br>With Our Team</h2></div>
  <div class="handshake-photo" role="img" aria-label="Black and white photograph of two business people shaking hands over documents"></div>
  <div class="about">
    <p>Pelbury Solicitors is a private law firm based in Liverpool that has been servicing the Sydney area for over 30 years. With a dedicated, professional and friendly team we pride ourselves on delivering an exceptional legal service to our clients.</p>
    <p>Offering a complete legal service at affordable rates, our clients really do come first.</p>
  </div>
  <footer class="contact">
    <p class="contact__address">3/82 Tarrow Street, Liverpool, NSW 2170</p>
    <p class="contact__phone">(02) 9413 5862</p>
    <p class="contact__line">www.pelburysolicitors-example.com.au</p>
    <p class="contact__line">info@pelburysolicitors-example.com.au</p>
  </footer>
  <div class="flyer__base"></div>
</section>

</body>
</html>
```